Elegant Black Candle Label Design!

I need a 2.375" tall by 3.0" wide candle label design. I'm looking for simple and elegant. Black label with silver leaf border and lettering. Label needs to have the following information on it: Fern Hollow Candle Co. as the company name, scent name in the middle and in smaller font, it needs to say Made in USA, All Natural, 8oz. Attached photos are for inspiration.

Target Market(s)

People looking for high end, all natural candle fragrances

Industry/Entity Type

Candle-Spa

Colors

Designer to choose only greyscale colors for use in the design.

Requirements
Must have
• Company Name, Scent (ability to change scent names), All Natural, Made in USA, 8oz
Nice to have
• Black background, silver leaf border and silver leaf font. Elegant fonts maybe slightly cursive

```html
<!DOCTYPE html>
<html lang="en">
<head>
<meta charset="UTF-8">
<title>Fern Hollow Candle Co. — Candle Labels</title>
<link rel="stylesheet" href="https://fonts.googleapis.com/css2?family=Questrial&family=Playfair+Display:ital@1&family=Cedarville+Cursive&display=swap">
<style>
  :root {
    --backdrop: #d9d3ce;
    --label-black: #0c0b0b;
    --silver: #bdbdbd;
    --silver-soft: #8f8f8f;
    --silver-light: #e2e2e2;
    --gold: #b99c66;
    --gold-soft: #8a7346;
    --gold-light: #d8c08e;
  }
  * { margin: 0; padding: 0; box-sizing: border-box; }
  html, body {
    width: 1200px;
    height: 1000px;
    overflow: hidden;
    background: var(--backdrop);
  }
  .canvas {
    position: relative;
    width: 1200px;
    height: 1000px;
  }
  .label {
    position: absolute;
    top: 257px;
    width: 443px;
    height: 559px;
    background: var(--label-black);
    --ink: var(--silver);
    --ink-soft: var(--silver-soft);
    --ink-light: var(--silver-light);
  }
  .label--silver { left: 157px; }
  .label--gold {
    left: 635px;
    --ink: var(--gold);
    --ink-soft: var(--gold-soft);
    --ink-light: var(--gold-light);
  }
  .frame { position: absolute; inset: 0; }
  .frame rect { fill: none; stroke: var(--ink-soft); stroke-width: 1; }

  .leaf-corner {
    position: absolute;
    width: 196px;
    height: 62px;
    opacity: 0.55;
  }
  .leaf-corner--top {
    left: 31px; top: 26px;
    background: linear-gradient(160deg, var(--ink-light) 0%, transparent 75%);
    border-radius: 0 0 90% 0;
  }
  .leaf-corner--bottom {
    right: 31px; bottom: 26px;
    background: linear-gradient(340deg, var(--ink-light) 0%, transparent 75%);
    border-radius: 90% 0 0 0;
  }

  .brand {
    position: absolute;
    left: 0; right: 0;
    top: 110px;
    text-align: center;
    font-family: 'Questrial', sans-serif;
    font-size: 22px;
    letter-spacing: 3px;
    color: var(--ink);
  }
  .rule {
    position: absolute;
    left: 87px;
    width: 269px;
    height: 1px;
    background: var(--ink-soft);
  }
  .rule--top { top: 199px; }
  .rule--bottom { top: 383px; }

  .scent-name {
    position: absolute;
    left: 0; right: 0;
    top: 228px;
    text-align: center;
    font-family: 'Playfair Display', serif;
    font-style: italic;
    font-size: 44px;
    color: var(--ink);
  }
  .scent-notes {
    position: absolute;
    left: 0; right: 0;
    top: 288px;
    text-align: center;
    font-family: 'Cedarville Cursive', cursive;
    font-size: 12px;
    color: var(--ink);
  }
  .scent-description {
    position: absolute;
    left: 118px;
    width: 207px;
    top: 296px;
    text-align: center;
    font-family: 'Questrial', sans-serif;
    font-size: 9px;
    line-height: 12.5px;
    color: var(--ink);
  }

  .claims {
    position: absolute;
    left: 0; right: 0;
    top: 420px;
    display: flex;
    justify-content: center;
    align-items: center;
    font-family: 'Questrial', sans-serif;
    font-size: 12.5px;
    letter-spacing: 2px;
    color: var(--ink);
  }
  .claims__divider {
    width: 1px;
    height: 22px;
    background: var(--ink-soft);
    margin: 0 15px;
  }
  .net-weight {
    position: absolute;
    left: 0; right: 0;
    top: 456px;
    text-align: center;
    font-family: 'Questrial', sans-serif;
    font-size: 13px;
    color: var(--ink);
  }
</style>
</head>
<body>
<main class="canvas">

  <section class="label label--silver">
    <svg class="frame" width="443" height="559" viewBox="0 0 443 559">
      <rect x="21.5" y="21.5" width="400" height="516"/>
      <rect x="31.5" y="31.5" width="380" height="496"/>
    </svg>
    <div class="leaf-corner leaf-corner--top" role="img" aria-label="Silver leaf branch ornament"></div>
    <div class="leaf-corner leaf-corner--bottom" role="img" aria-label="Silver leaf branch ornament"></div>
    <p class="brand">Fern Hollow Candle Co.</p>
    <div class="rule rule--top"></div>
    <h1 class="scent-name">Scent Name</h1>
    <p class="scent-notes">Cinamon | Smoke | Sandalwood</p>
    <div class="rule rule--bottom"></div>
    <div class="claims">
      <span>ALL NATURAL</span>
      <span class="claims__divider"></span>
      <span>MADE IN USA</span>
    </div>
    <p class="net-weight">8oz</p>
  </section>

  <section class="label label--gold">
    <svg class="frame" width="443" height="559" viewBox="0 0 443 559">
      <rect x="21.5" y="21.5" width="400" height="516"/>
      <rect x="31.5" y="31.5" width="380" height="496"/>
    </svg>
    <div class="leaf-corner leaf-corner--top" role="img" aria-label="Gold leaf branch ornament"></div>
    <div class="leaf-corner leaf-corner--bottom" role="img" aria-label="Gold leaf branch ornament"></div>
    <p class="brand">Fern Hollow Candle Co.</p>
    <div class="rule rule--top"></div>
    <h2 class="scent-name">Scent Name</h2>
    <p class="scent-description">Nulla tellus sem, viverra eu, ultricies ac, mattis et, velit. Maecenas quis magna. Ut viverra nisl eu ipsum. Maecenas rhoncus. Duis mattis nisi nec</p>
    <div class="rule rule--bottom"></div>
    <div class="claims">
      <span>ALL NATURAL</span>
      <span class="claims__divider"></span>
      <span>MADE IN USA</span>
    </div>
    <p class="net-weight">8oz</p>
  </section>

</main>
</body>
</html>
```